luxury contemporary fashion website needs simple, elegant flowchart to describe the buying and selli

* Luxury, resale, preloved items are sold on this online platform
*Horizontal, simple, flowchart with 5 steps in 'friendly' font with a simple emoticon/ picture for each step
*To be positioned in the 'How we work' tab of the webpage to explain in a very simple manner the buying and selling process for the customers.
*Attached is a very rudimentary mock-up of what we would like included and an idea of a project similar to what we desire
* to confirm the text for each step, we have also attached a word file below

Industry/Entity Type

Fashion

Font styles to use
Sans Serif

Colors
86cfc6
cfeae6

Requirements
Must have
• Simple drawing / shape after each point In the closest to 'duck egg blue' fill colour you can find with a black outline

```html
<!DOCTYPE html>
<html lang="en">
<head>
<meta charset="utf-8">
<title>How we work</title>
<link rel="stylesheet" href="https://fonts.googleapis.com/css2?family=Questrial&family=Mulish:wght@700&display=swap">
<style>
  :root {
    --teal: #86cfc6;
    --duck-egg: #cfeae6;
    --cloud-text: #eaf7f5;
    --bg-centre: #666a6f;
    --bg-edge: #34373b;
  }
  * { margin: 0; padding: 0; box-sizing: border-box; }
  html, body { width: 1200px; height: 758px; overflow: hidden; }
  body {
    position: relative;
    background: radial-gradient(ellipse 720px 520px at 600px 380px, var(--bg-centre) 0%, var(--bg-edge) 100%);
    font-family: "Questrial", sans-serif;
    color: var(--teal);
  }
  .step-disc {
    position: absolute;
    width: 116px; height: 116px;
    border-radius: 50%;
    background: var(--duck-egg);
    border: 2px solid var(--teal);
    box-shadow: 0 10px 14px rgba(0,0,0,0.35);
    display: flex; align-items: center; justify-content: center;
  }
  .step-disc svg { width: 70px; height: 70px; }
  .step-number {
    position: absolute;
    width: 32px; height: 32px;
    border-radius: 50%;
    background: var(--teal);
    color: var(--cloud-text);
    font-family: "Mulish", sans-serif;
    font-weight: 700;
    font-size: 20px;
    display: flex; align-items: center; justify-content: center;
    box-shadow: 0 0 0 3px rgba(207,234,230,0.55);
  }
  .step-caption {
    position: absolute;
    width: 220px;
    text-align: center;
    transform: translateX(-50%);
  }
  .step-title {
    font-family: "Mulish", sans-serif;
    font-weight: 700;
    font-size: 15px;
    line-height: 20px;
  }
  .step-text { font-size: 11.5px; line-height: 14px; }
  .chevron { position: absolute; width: 24px; height: 44px; }
  .payment-cloud { position: absolute; left: 820px; top: 295px; width: 150px; height: 130px; }
  .payment-label {
    position: absolute; left: 820px; top: 328px; width: 150px;
    text-align: center;
    font-size: 21px; line-height: 27px;
    color: var(--cloud-text);
  }
  .outcome-arrows { position: absolute; left: 940px; top: 285px; width: 50px; height: 145px; }
  .currency-glyphs {
    font-family: "Mulish", sans-serif; font-weight: 700;
    color: var(--teal); font-size: 34px; letter-spacing: -1px;
  }
  .currency-glyphs .dollar { font-size: 50px; }
</style>
</head>
<body>

<svg width="0" height="0" style="position:absolute">
  <defs>
    <linearGradient id="chevron-fill" x1="0" y1="0" x2="1" y2="0">
      <stop offset="0" stop-color="#ffffff" stop-opacity="0.35"/>
      <stop offset="1" stop-color="#ffffff" stop-opacity="0.9"/>
    </linearGradient>
  </defs>
</svg>

<!-- Step 1 -->
<div class="step-disc" style="left:100px;top:305px;">
  <svg viewBox="0 0 70 70" aria-label="Basket">
    <path d="M22 28 L30 14 M48 28 L40 14" stroke="var(--teal)" stroke-width="4" stroke-linecap="round" fill="none"/>
    <rect x="8" y="26" width="54" height="7" rx="2" fill="var(--teal)"/>
    <path d="M12 35 H58 L53 56 H17 Z" fill="var(--teal)"/>
    <path d="M24 39 V52 M31 39 V52 M39 39 V52 M46 39 V52" stroke="var(--duck-egg)" stroke-width="3" stroke-linecap="round"/>
  </svg>
</div>
<div class="step-number" style="left:108px;top:302px;">1</div>
<div class="step-caption" style="left:158px;top:430px;">
  <div class="step-title">Have items to sell?</div>
  <div class="step-text">brand spanking or nearly new ✶</div>
</div>

<svg class="chevron" style="left:246px;top:348px;" viewBox="0 0 24 44"><path d="M2 2 L22 22 L2 42 L6 22 Z" fill="url(#chevron-fill)"/></svg>

<!-- Step 2 -->
<div class="step-disc" style="left:292px;top:305px;">
  <svg viewBox="0 0 70 70" aria-label="Clothing and accessories">
    <path d="M10 14 L16 14 L19 22 L22 14 L28 14 L26 30 L30 54 L8 54 L12 30 Z" fill="var(--teal)"/>
    <path d="M36 26 Q40 18 44 26" stroke="var(--teal)" stroke-width="2" fill="none"/>
    <rect x="33" y="26" width="14" height="16" fill="var(--teal)"/>
    <circle cx="56" cy="32" r="8" fill="none" stroke="var(--teal)" stroke-width="2"/>
    <path d="M56 28 V32 H59" stroke="var(--teal)" stroke-width="1.5" fill="none"/>
    <ellipse cx="40" cy="50" rx="6" ry="4" fill="var(--teal)"/>
    <ellipse cx="54" cy="50" rx="6" ry="4" fill="var(--teal)"/>
    <path d="M46 49 H48" stroke="var(--teal)" stroke-width="2"/>
  </svg>
</div>
<div class="step-number" style="left:297px;top:302px;">2</div>
<div class="step-caption" style="left:350px;top:430px;">
  <div class="step-title">Personal collection</div>
  <div class="step-text">we choose the pieces we know<br>thelumeno customers will love ♥</div>
</div>

<svg class="chevron" style="left:437px;top:348px;" viewBox="0 0 24 44"><path d="M2 2 L22 22 L2 42 L6 22 Z" fill="url(#chevron-fill)"/></svg>

<!-- Step 3 -->
<div class="step-disc" style="left:491px;top:305px;">
  <svg viewBox="0 0 70 70" aria-label="Shopping cart">
    <path d="M6 14 H14 L22 48 H58" stroke="var(--teal)" stroke-width="4" fill="none" stroke-linejoin="round"/>
    <path d="M15 22 H60 L55 40 H20" stroke="var(--teal)" stroke-width="3" fill="none"/>
    <rect x="30" y="14" width="22" height="22" fill="var(--teal)"/>
    <path d="M41 14 V36 M30 25 H52" stroke="var(--duck-egg)" stroke-width="2"/>
    <circle cx="26" cy="56" r="5" fill="var(--teal)"/>
    <circle cx="52" cy="56" r="5" fill="var(--teal)"/>
  </svg>
</div>
<div class="step-number" style="left:488px;top:302px;">3</div>
<div class="step-caption" style="left:550px;top:430px;">
  <div class="step-title">We prepare</div>
  <div class="step-text">your item for sale with thorough<br>authenticity &amp; condition checks...<br>so you don’t have to! ◡</div>
</div>

<svg class="chevron" style="left:635px;top:348px;" viewBox="0 0 24 44"><path d="M2 2 L22 22 L2 42 L6 22 Z" fill="url(#chevron-fill)"/></svg>

<!-- Step 4 -->
<div class="step-disc" style="left:680px;top:305px;">
  <svg viewBox="0 0 70 70" aria-label="Hand trolley with boxes">
    <path d="M20 6 L24 8 L34 56 L54 52" stroke="var(--teal)" stroke-width="4" fill="none" stroke-linejoin="round"/>
    <rect x="30" y="12" width="16" height="14" transform="rotate(-12 38 19)" fill="var(--teal)"/>
    <rect x="33" y="28" width="16" height="12" transform="rotate(-12 41 34)" fill="var(--teal)"/>
    <rect x="36" y="41" width="16" height="10" transform="rotate(-12 44 46)" fill="var(--teal)"/>
    <circle cx="32" cy="60" r="5" fill="var(--teal)"/>
  </svg>
</div>
<div class="step-number" style="left:680px;top:302px;">4</div>
<div class="step-caption" style="left:739px;top:430px;">
  <div class="step-title">Once sold</div>
  <div class="step-text">we lovingly prepare the item<br>shipped via tracked services ✈</div>
</div>

<!-- Step 5 -->
<svg class="payment-cloud" viewBox="0 0 150 130" aria-hidden="true">
  <g fill="var(--teal)">
    <circle cx="40" cy="35" r="28"/>
    <circle cx="78" cy="28" r="26"/>
    <circle cx="112" cy="42" r="26"/>
    <circle cx="122" cy="78" r="24"/>
    <circle cx="95" cy="102" r="24"/>
    <circle cx="55" cy="102" r="24"/>
    <circle cx="26" cy="80" r="24"/>
    <rect x="30" y="35" width="95" height="70"/>
  </g>
</svg>
<div class="payment-label">Your<br>Payment</div>
<div class="step-number" style="left:827px;top:302px;">5</div>

<svg class="outcome-arrows" viewBox="0 0 50 145" aria-hidden="true">
  <path d="M4 34 L28 18" stroke="var(--teal)" stroke-width="4"/>
  <path d="M22 10 L36 10 L30 23 Z" fill="var(--teal)"/>
  <path d="M4 108 L28 124" stroke="var(--teal)" stroke-width="4"/>
  <path d="M22 132 L36 134 L32 120 Z" fill="var(--teal)"/>
</svg>

<!-- Outcome: cash -->
<div class="step-disc" style="left:988px;top:147px;width:120px;height:120px;">
  <div class="currency-glyphs">£<span class="dollar">$</span>€</div>
</div>
<div class="step-caption" style="left:1048px;top:271px;">
  <div class="step-title">Pocket the cash</div>
  <div class="step-text">get amount for your item</div>
</div>

<!-- Outcome: charity -->
<div class="step-disc" style="left:990px;top:420px;">
  <svg viewBox="0 0 70 70" aria-label="Heart">
    <path d="M35 60 C10 42 6 30 8 22 C11 11 27 8 35 20 C43 8 59 11 62 22 C64 30 60 42 35 60 Z" fill="var(--teal)"/>
    <path d="M20 34 L32 44 M28 28 L42 40 M40 30 L50 38" stroke="var(--duck-egg)" stroke-width="3" stroke-linecap="round"/>
  </svg>
</div>
<div class="step-caption" style="left:1048px;top:545px;">
  <div class="step-title">Donate to charity</div>
  <div class="step-text">full or partial amount ☺</div>
</div>

</body>
</html>
```